The Halvern Clinic Business Card

We need a new business card design for a rehabilitation center in California. Please use the branding from the logo.

Use the attached logo.

Target Market(s)

Physicians referring patients

Industry/Entity Type

Business

Contact Information for Business Card

Updated business cards for new brand

Font styles to use
Sans Serif

Colors
0255a3
3176b5
85abd2
fece3e

Requirements
Must have
• The logo: front and back
• website url: www.TheHalvernClinic.example
• Full Name: Daniel Porthouse
• Title: Chief Financial Officer
• Email: dporthouse@thehalvernclinic.example
• Office: 555.412.7730
• Cell: 555.639.2184
• Fax: 555.207.5518
Nice to have
• Icons
Should not have
• whimsical fonts

```html
<!DOCTYPE html>
<html lang="en">
<head>
<meta charset="utf-8">
<title>The Halvern Clinic Business Card</title>
<link href="https://fonts.googleapis.com/css2?family=Arimo:wght@400;700&display=swap" rel="stylesheet">
<style>
  :root {
    --brand-blue: #3176b5;
    --ink: #231f20;
    --paper: #ffffff;
    --edge: #8a8a8a;
  }
  * { margin: 0; padding: 0; box-sizing: border-box; }
  html, body {
    width: 1200px; height: 1200px; overflow: hidden;
    background: var(--paper);
    font-family: "Arimo", Arial, sans-serif;
  }
  .canvas { position: relative; width: 1200px; height: 1200px; }

  .card {
    position: absolute; left: 180px; width: 838px; height: 479px;
    border-radius: 40px;
  }
  .card--front { top: 100px; background: var(--brand-blue); color: var(--paper); }
  .card--back { top: 619px; background: var(--paper); border: 1px solid var(--edge); color: var(--ink); }

  .wordmark {
    position: absolute; display: flex; align-items: center; gap: 22px;
    font-weight: 700; white-space: nowrap; letter-spacing: -0.5px;
  }
  .wordmark__square { flex: none; background: currentColor; }

  .card--front .wordmark { left: 50%; top: 205px; transform: translateX(-50%); font-size: 60px; }
  .card--front .wordmark__square { width: 54px; height: 54px; }
  .front-url {
    position: absolute; left: 0; right: 0; top: 408px; text-align: center;
    font-size: 25px;
  }

  .card--back .wordmark { right: 54px; top: 82px; font-size: 44px; color: var(--brand-blue); }
  .card--back .wordmark__square { width: 40px; height: 40px; }

  .person { position: absolute; left: 54px; top: 225px; }
  .person__name { font-size: 32px; font-weight: 700; line-height: 1.1; }
  .person__title { font-size: 22px; margin-top: 4px; }

  .contact-list { position: absolute; list-style: none; }
  .contact-list li { display: flex; align-items: center; height: 35.5px; }
  .contact-list svg { flex: none; fill: var(--brand-blue); }
  .contact-list--phones { left: 54px; top: 329px; font-size: 26px; }
  .contact-list--phones svg { width: 26px; height: 26px; margin-right: 16px; }
  .contact-list--online { left: 366px; top: 364px; font-size: 22px; }
  .contact-list--online svg { width: 24px; height: 24px; margin-right: 16px; }
</style>
</head>
<body>
<main class="canvas">

  <section class="card card--front" aria-label="Card front">
    <div class="wordmark"><span class="wordmark__square"></span>The Halvern Clinic</div>
    <p class="front-url">www.TheHalvernClinic.example</p>
  </section>

  <section class="card card--back" aria-label="Card back">
    <div class="wordmark"><span class="wordmark__square"></span>The Halvern Clinic</div>

    <div class="person">
      <h1 class="person__name">Daniel Porthouse</h1>
      <p class="person__title">Chief Financial Officer</p>
    </div>

    <ul class="contact-list contact-list--phones">
      <li>
        <svg viewBox="0 0 26 26" aria-label="Office"><path d="M1 12c3-6 21-6 24 0l-1 3-5-1-1-3c-3-1-7-1-10 0l-1 3-5 1z"/><circle cx="13" cy="17" r="5"/></svg>
        555.412.7730
      </li>
      <li>
        <svg viewBox="0 0 26 26" aria-label="Cell"><path d="M7 1h12a2 2 0 0 1 2 2v20a2 2 0 0 1-2 2H7a2 2 0 0 1-2-2V3a2 2 0 0 1 2-2zm1 3v14h10V4z"/><circle cx="13" cy="21.5" r="1.5" fill="#fff"/></svg>
        555.639.2184
      </li>
      <li>
        <svg viewBox="0 0 26 26" aria-label="Fax"><path d="M7 1h11v14H7zM3 16h20v6H3zM2 23h22v2H2z"/><path d="M9 4h7v1.5H9zM9 7h7v1.5H9zM9 10h7v1.5H9z" fill="#fff"/></svg>
        555.207.5518
      </li>
    </ul>

    <ul class="contact-list contact-list--online">
      <li>
        <svg viewBox="0 0 24 24" aria-label="Email"><path d="M1 5h22v14H1z"/><path d="M2 6l10 7 10-7M2 18l7-6M22 18l-7-6" stroke="#fff" stroke-width="1.6" fill="none"/></svg>
        dporthouse@thehalvernclinic.example
      </li>
      <li>
        <svg viewBox="0 0 24 24" aria-label="Website"><circle cx="12" cy="12" r="11"/><g stroke="#fff" stroke-width="1.5" fill="none"><ellipse cx="12" cy="12" rx="4.5" ry="10"/><path d="M2 12h20M12 2v20M4 7h16M4 17h16"/></g></svg>
        www.TheHalvernClinic.example
      </li>
    </ul>
  </section>

</main>
</body>
</html>
```